TRIVAN 2026 Flyer for Conference

TRIVAN needs a design for a 1-page flyer that we will hand out at an upcoming event & then later post online as a pdf. There are 3 elements which need to be on the flyer:

1) A logo. This should be prominent on the design (e.g., in the middle). The flyer should use the colors that are in that logo (e.g., for accents, design elements, and/or text; not all of these have to be used):
Dark blue: #185577
Med blue: #327C9A
Teal: #4EB1C2
Light Teal: #9EDBE6

2) The conference theme -- Forests of Wonder: Climbing toward Research Fluency -- should be at the flyer's top.

3) Finally, these six tracks should be listed below the theme and the logo (it's font size should be at least a couple sizes smaller than the size used for the theme):
- Pearls of Pedagogy: Teaching Techniques that Work
- The Depth Gauge: Measuring Instructional Impact
- Techtonic Shifts: Innovation and Educational Technology
- Captain's Log: Navigating Leadership in Library Instruction
- Swimming Together: Collaborating with Others
- The Bermuda Triangle: Exploring (Seemingly) Eternal Challenges

Font styles to use
Sans Serif

Colors
0094D4
00A9DD
6FCCEA
C7EBF8
E9F6FB

Requirements
Must have
• The 3 elements listed in the description: 1) the logo, 2) the text of the theme and 3) the text for the tracks.

```html
<!DOCTYPE html>
<html lang="en">
<head>
<meta charset="utf-8">
<title>TRIVAN 2026 – Forests of Wonder</title>
<link rel="stylesheet" href="https://fonts.googleapis.com/css2?family=Poppins:wght@400;500;600;700;800&family=Dancing+Script:wght@700&display=swap">
<style>
  :root {
    --page-bg: #163f4d;
    --dark-blue: #185577;
    --med-blue: #327C9A;
    --teal: #4EB1C2;
    --light-teal: #9EDBE6;
    --sky-top: #8fe6e8;
    --sky-mid: #dff7f8;
    --title-ink: #124a63;
    --number-ink: #3b6f8f;
    --label-ink: #1b2b35;
    --white: #ffffff;
  }
  * { margin: 0; padding: 0; box-sizing: border-box; }
  html, body {
    width: 1010px; height: 1200px; overflow: hidden;
    background: var(--page-bg);
    font-family: 'Poppins', sans-serif;
  }
  .flyer {
    position: absolute; left: 41px; top: 0;
    width: 928px; height: 1200px;
    background: linear-gradient(180deg, var(--sky-top) 0%, var(--sky-mid) 30%, var(--white) 60%, var(--white) 70%, var(--dark-blue) 70%);
    overflow: hidden;
  }
  .sky-glow {
    position: absolute; inset: 0 0 auto 0; height: 840px;
    background: radial-gradient(ellipse at 50% 30%, rgba(255,255,255,0.85) 0%, rgba(255,255,255,0) 60%);
  }
  .brand {
    position: absolute; top: 84px; left: 0; width: 100%;
    display: flex; justify-content: center; align-items: center; gap: 12px;
  }
  .brand-dot {
    width: 38px; height: 38px; border-radius: 50%;
    background: var(--teal);
  }
  .brand-name {
    font-weight: 700; font-size: 44px; letter-spacing: 1px;
    color: var(--dark-blue); line-height: 1;
  }
  .theme {
    position: absolute; top: 188px; left: 0; width: 100%;
    text-align: center; color: var(--title-ink);
  }
  .theme-line {
    display: block; font-weight: 800; line-height: 1;
    letter-spacing: -2px;
  }
  .theme-top { font-size: 104px; }
  .theme-bottom { font-size: 120px; margin-top: 6px; }
  .theme-joiner {
    position: absolute; left: 50%; top: 82px; transform: translateX(-50%);
    font-family: 'Dancing Script', cursive; font-weight: 700;
    font-size: 52px; color: var(--teal); line-height: 1;
  }
  .theme-sub {
    position: absolute; top: 398px; left: 0; width: 100%;
    text-align: center; font-weight: 700; font-size: 29px;
    letter-spacing: 4px; color: var(--teal);
  }
  .wave-art {
    position: absolute; left: 0; top: 440px; width: 100%; height: 410px;
    background:
      linear-gradient(180deg, rgba(158,219,230,0) 0%, rgba(158,219,230,0.9) 22%, var(--teal) 55%, var(--med-blue) 80%, var(--dark-blue) 100%);
  }
  .tracks {
    position: absolute; top: 873px; left: 0; width: 100%;
  }
  .track {
    position: absolute; width: 420px; height: 80px;
  }
  .track-num {
    position: absolute; left: 0; top: -8px;
    font-weight: 700; font-size: 46px; line-height: 1;
    color: var(--number-ink); letter-spacing: -1px;
  }
  .track-label {
    position: absolute; left: 66px; top: 0; width: 272px; height: 32px;
    border-radius: 3px; padding-left: 16px;
    font-weight: 700; font-size: 21px; line-height: 32px;
    color: var(--label-ink); white-space: nowrap;
  }
  .track-label.is-teal { background: var(--teal); }
  .track-label.is-light { background: var(--light-teal); }
  .track-desc {
    position: absolute; left: 66px; top: 41px;
    font-weight: 500; font-size: 16px; color: var(--white); white-space: nowrap;
  }
  .col-left { left: 59px; }
  .col-right { left: 473px; }
  .site {
    position: absolute; top: 1130px; left: 0; width: 100%;
    display: flex; align-items: center; gap: 12px;
  }
  .site-rule { flex: 1; height: 1px; background: var(--light-teal); }
  .site-url {
    font-size: 18px; letter-spacing: 3.5px; color: var(--white);
    font-weight: 400;
  }
  .site-url strong { font-weight: 700; }
</style>
</head>
<body>
  <main class="flyer">
    <div class="sky-glow"></div>

    <div class="brand">
      <span class="brand-name">TRIVAN 2026</span>
      <span class="brand-dot"></span>
    </div>

    <h1 class="theme">
      <span class="theme-line theme-top">FORESTS</span>
      <span class="theme-joiner">of</span>
      <span class="theme-line theme-bottom">WONDER</span>
    </h1>
    <p class="theme-sub">CLIMBING TOWARD RESEARCH FLUENCY</p>

    <div class="wave-art" role="img" aria-label="Illustration of a large curling ocean wave with white foam, spray and rolling water"></div>

    <section class="tracks">
      <div class="track col-left" style="top:0">
        <span class="track-num">01</span>
        <span class="track-label is-teal">PEARLS OF PEDAGOGY</span>
        <span class="track-desc">Teaching Techniques that Work</span>
      </div>
      <div class="track col-left" style="top:84px">
        <span class="track-num">02</span>
        <span class="track-label is-light">THE DEPTH GAUGE</span>
        <span class="track-desc">Measuring Instructional Impact</span>
      </div>
      <div class="track col-left" style="top:166px">
        <span class="track-num">03</span>
        <span class="track-label is-teal">TECHTONIC SHIFTS</span>
        <span class="track-desc">Innovation and Educational Technology</span>
      </div>
      <div class="track col-right" style="top:0">
        <span class="track-num">04</span>
        <span class="track-label is-light">CAPTAIN’S LOG</span>
        <span class="track-desc">Navigating Leadership in Library Instruction</span>
      </div>
      <div class="track col-right" style="top:84px">
        <span class="track-num">05</span>
        <span class="track-label is-teal">SWIMMING TOGETHER</span>
        <span class="track-desc">Collaborating with Others</span>
      </div>
      <div class="track col-right" style="top:166px">
        <span class="track-num">06</span>
        <span class="track-label is-light">THE BARMUDA TRIANGLE</span>
        <span class="track-desc">Exploring (Seemingly) Eternal Challenges</span>
      </div>
    </section>

    <footer class="site">
      <span class="site-rule"></span>
      <span class="site-url">www.<strong>trivanconference2026</strong>.com</span>
      <span class="site-rule"></span>
    </footer>
  </main>
</body>
</html>
```